Cover Page Design

Create a new cover page in a sleek modern look that consists of our logo as provided. This cover page will be used in presentations and should only have colors featured in our branding efforts.

Target Market(s)

Architectural and Interior Design Clients

Industry/Entity Type

Interior Design

Font styles to use
Other font styles liked:
• see attached logo

Colors

Designer to choose colors to be used in the design.

Requirements
Must have
• Clean look, no pictures. just logo.
Nice to have
• colors that relate to our brand.
Should not have
• No colors not featured in our branding:
• www.velmacardwick.com

```html
<!DOCTYPE html>
<html lang="en">
<head>
<meta charset="utf-8">
<title>Velma Cardwick + Partners — Presentation Cover</title>
<link rel="stylesheet" href="https://fonts.googleapis.com/css2?family=Jost:wght@300&display=swap">
<style>
  :root {
    --brand-blue: #0075bf;
    --pale-blue-start: #e4f0f9;
    --pale-blue-end: #b3d6ec;
    --ink: #231f20;
    --paper: #ffffff;
  }
  html, body {
    margin: 0;
    padding: 0;
    overflow: hidden;
    background: var(--paper);
  }
  .cover {
    position: relative;
    width: 848px;
    height: 1200px;
    overflow: hidden;
    background: var(--paper);
    font-family: "Jost", "Helvetica Neue", Arial, sans-serif;
    font-weight: 300;
    color: var(--ink);
  }
  .backdrop-disc {
    position: absolute;
    left: 0;
    top: 0;
    width: 848px;
    height: 1200px;
  }
  .brand-block {
    position: absolute;
    left: 0;
    top: 978px;
    width: 848px;
    height: 150px;
  }
  .brand-dot {
    position: absolute;
    left: 258px;
    top: 0;
    width: 104px;
    height: 104px;
    border-radius: 50%;
    background: var(--brand-blue);
  }
  .brand-name {
    position: absolute;
    left: 377px;
    top: 22px;
    width: 376px;
    margin: 0;
    font-size: 35px;
    font-weight: 300;
    line-height: 1;
    letter-spacing: 0.02em;
    white-space: nowrap;
    color: var(--ink);
  }
  .brand-partners {
    position: absolute;
    left: 570px;
    top: 68px;
    width: 195px;
    margin: 0;
    font-size: 11px;
    font-weight: 300;
    letter-spacing: 1.15em;
    white-space: nowrap;
    color: var(--ink);
  }
  .brand-rule {
    position: absolute;
    left: 359px;
    top: 97px;
    width: 489px;
    height: 3px;
    background: linear-gradient(to right, rgba(0,117,191,0), var(--brand-blue) 75%);
  }
  .services {
    position: absolute;
    left: 377px;
    top: 120px;
    margin: 0;
    font-size: 11px;
    font-weight: 300;
    letter-spacing: 0.46em;
    white-space: nowrap;
    color: var(--ink);
  }
</style>
</head>
<body>
  <main class="cover">
    <svg class="backdrop-disc" viewBox="0 0 848 1200" aria-hidden="true">
      <defs>
        <linearGradient id="disc-fade" x1="0" y1="0" x2="1" y2="0">
          <stop offset="0" stop-color="var(--pale-blue-start)" stop-color-fallback="#e4f0f9"/>
          <stop offset="1" stop-color="#b3d6ec"/>
        </linearGradient>
      </defs>
      <circle cx="170" cy="470" r="433" fill="url(#disc-fade)" opacity="0.9"/>
    </svg>

    <section class="brand-block">
      <span class="brand-dot" aria-hidden="true"></span>
      <h1 class="brand-name">VELMA CARDWICK</h1>
      <p class="brand-partners">+ PARTNERS</p>
      <span class="brand-rule" aria-hidden="true"></span>
      <p class="services">ARCHITECTURE | INTERIOR DESIGN</p>
    </section>
  </main>
</body>
</html>
```